Clausewise - Training I Consulting I Review - Related to Contracts/Agreements

We provide legal services, we need a plattform to book video online trainings or local trainings classes and appointments (with calendar feature to select date and see availability at screen), payment over internet, legal document creation over webpage, videos will be produces in the next 3 - 4 moths so this is a place holder item. Participants for the Online trainings shall have a login in area with secured password. Appointments for local trainings and Consulting. Consider Outline in file attached. I can send you also a video with more explanation regarding the purpose.

Target Market(s)

Startup/scale up Software companies that intent to have an international business and need help with their contracts, to sell their products. Sales persons.

Industry/Entity Type

Legal

Coding

Coded - Design and coding required

Number of Pages Required

5+ page

Font styles to use
Serif
Sans Serif

Colors
000000
eeeeee
f5f5f5
ffffff
f8fcfd
3277b5
ecf7fb
cadf82
86cfc6

Requirements
Must have
• See file clausewise attached with outline. Moreover see here first starting point: https://tomas-vendrell.pagebuildr.example/mysite-1 . Main inspiration comes from www.advisoryhub.example from the log in area, see the outline in the file attached with the screen shots. At the end I need someone who can draft the full webpage and maintain it for a yearly fee. It must be simple and well structured layout. Lean. 1st landing page shall not scroll, 2 landing page only a little to see the testimonials and foster of page. There should be a Progress Bar to indicate the booking/selection process. Calendar booking. Easy fast booking.
• I like the colour mix, the feeling and the easy structor of:
• https://www.artmarket.example/design/6374387or
• https://www.artmarket.example/design/6372391 or https://www.artmarket.example/design/6374366
• https://www.vendorgrid.example/en/web-design/belgium-be
• https://www.artmarket.example/design/5896857
• https://www.artmarket.example/design/5902173
• https://www.artmarket.example/design/17197349
• https://www.artmarket.example/design/5464461
• https://www.artmarket.example/design/7180908
Nice to have
• page for evaluation and interview, see outline attached in the file with screen shots. Document upload.
Should not have
• many pictures, long scroll down pages on the 1st and 2nd ladding pages, many colours and forms. No need for news letter, search field, no need for links to Chatterly and other social media (except workNet).

```html
<!DOCTYPE html>
<html lang="en">
<head>
<meta charset="utf-8">
<title>Clausewise – Training, Design, Review</title>
<link rel="stylesheet" href="https://fonts.googleapis.com/css2?family=Montserrat:wght@200;300&family=Open+Sans:wght@400;600;700&display=swap">
<style>
:root{
  --ink:#1b1b1b;
  --hero:#1e1e1e;
  --footer:#1d1d1d;
  --base:#161616;
  --lime:#cadf82;
  --red:#e41f26;
  --white:#ffffff;
  --muted:#8c8c8c;
  --text:#555555;
  --line:#eeeeee;
}
*{margin:0;padding:0;box-sizing:border-box}
html,body{width:764px;height:1200px;overflow:hidden}
body{position:relative;background:var(--white);font-family:'Open Sans',Arial,sans-serif;color:var(--ink)}
.abs{position:absolute}
.hero{left:0;top:0;width:764px;height:305px;background:linear-gradient(180deg,#1c1c1c 0%,#1f1f1f 55%,#262626 100%)}
.hero-backdrop{left:0;top:150px;width:764px;height:155px;background:linear-gradient(180deg,rgba(40,40,40,0) 0%,rgba(48,48,48,.7) 100%)}
.brand{font-family:'Montserrat',Arial,sans-serif;font-weight:300;color:var(--white);font-size:15px;letter-spacing:.5px;white-space:nowrap}
.nav{top:17px;left:381px;display:flex;gap:14px;font-size:6.5px;font-weight:600;letter-spacing:.4px;white-space:nowrap}
.nav a{color:var(--muted);text-decoration:none}
.nav a.active{color:var(--lime)}
.btn-lime{background:var(--lime);color:var(--ink);font-weight:700;font-size:7.5px;letter-spacing:.5px;display:flex;align-items:center;justify-content:center;border-radius:2px}
.hero-title{top:105px;width:764px;text-align:center;font-family:'Montserrat',Arial,sans-serif;font-weight:200;color:var(--white);font-size:28px;letter-spacing:1.5px}
.hero-sub{top:145px;width:764px;text-align:center;color:var(--white);font-weight:600;font-size:11.5px;word-spacing:3px;letter-spacing:.3px}
.section-title{width:764px;text-align:center;font-family:'Montserrat',Arial,sans-serif;font-weight:300;font-size:18.5px;letter-spacing:.5px;color:var(--ink)}
.service{top:364px;width:142px;height:221px;background:var(--white);box-shadow:0 0 4px rgba(0,0,0,.09)}
.service-head{height:77px;background:var(--hero);display:flex;align-items:center;justify-content:center}
.service-icon{width:56px;height:56px;border-radius:6px;background:radial-gradient(circle,rgba(202,223,130,.35),rgba(202,223,130,.08))}
.service h3{margin-top:16px;text-align:center;font-size:7.4px;font-weight:700;letter-spacing:.2px}
.service p{margin:7px 12px 0;text-align:center;font-size:5.2px;line-height:11px;color:var(--text)}
.btn-red{background:var(--red);color:var(--white);font-weight:700;font-size:6.2px;letter-spacing:.3px;display:flex;align-items:center;justify-content:center;border-radius:2px;height:17px;margin:10px auto 0}
.video{left:159px;top:611px;width:447px;height:184px;background:linear-gradient(135deg,#3d3d3d 0%,#5b5b5b 45%,#4a4a4a 70%,#3a3a3a 100%);box-shadow:0 14px 14px -8px rgba(0,0,0,.25)}
.video-bar{left:4px;bottom:15px;width:439px;height:2px;background:rgba(255,255,255,.35)}
.video-bar span{display:block;width:196px;height:2px;background:var(--red)}
.video-time{left:51px;bottom:5px;font-size:3.8px;color:var(--white)}
.contact{left:159px;top:814px;width:447px;height:42px;background:var(--red);color:var(--white);font-weight:700;letter-spacing:.2px}
.contact-text{white-space:nowrap;line-height:12px}
.contact-email{left:59px;top:15px;font-size:8.6px}
.contact-phone{left:272px;top:14px;font-size:9.2px}
.quote{top:919px;width:142px;height:108px;background:var(--white);box-shadow:0 0 5px rgba(0,0,0,.1);text-align:center}
.quote p{margin:17px 10px 0;font-size:5.9px;line-height:12px;color:#333}
.stars{margin-top:1px;font-size:6.5px;color:#c4c4c4;letter-spacing:.5px}
.quote h4{margin-top:2px;font-size:6.8px;font-weight:700;color:var(--red);letter-spacing:.3px}
.avatar{top:1005px;width:46px;height:46px;border-radius:50%;border:2px solid var(--white);box-shadow:0 2px 5px rgba(0,0,0,.3)}
.footer{left:0;top:1084px;width:764px;height:82px;background:linear-gradient(180deg,#1e1e1e,#252525)}
.footer a{position:absolute;color:#dddddd;font-size:6.2px;text-decoration:none;white-space:nowrap}
.footer a::before{content:"»";margin-right:5px;color:#cccccc}
.base{left:0;top:1166px;width:764px;height:34px;background:var(--base)}
.legal{right:159px;top:10px;text-align:right;color:var(--white);font-size:5.6px;line-height:9px;white-space:nowrap}
</style>
</head>
<body>

<header class="abs hero">
  <div class="abs hero-backdrop" role="img" aria-label="Faint mountain silhouettes in dark grey"></div>
  <div class="abs brand" style="left:160px;top:12px">Clausewise</div>
  <nav class="abs nav">
    <a class="active" href="#">REFER SOMEONE</a>
    <a href="#">SERVICES</a>
    <a href="#">PARTNER</a>
  </nav>
  <a class="abs btn-lime" style="left:542px;top:12px;width:64px;height:19px">LOGIN</a>
  <h1 class="abs hero-title">CLAUSEWISE</h1>
  <div class="abs hero-sub">TRAINING &nbsp;/&nbsp; DESIGN &nbsp;/&nbsp; REVIEW</div>
  <a class="abs btn-lime" style="left:345px;top:177px;width:75px;height:22px">ENTER</a>
</header>

<h2 class="abs section-title" style="top:322px">CHOOSE YOUR SERVICE</h2>

<article class="abs service" style="left:159px">
  <div class="service-head"><div class="service-icon" role="img" aria-label="Line icon of a trainer presenting to a group"></div></div>
  <h3>CONTRACT TRAINING</h3>
  <p>Lorem Ipsum is simply dummy text of the printing and typesetting industry. Lorem Ipsum has been the industry's standard dummy text ever since the 1500s, when an unknown printer took a galley of type and scrambled it to make a type specimen book.</p>
  <a class="btn-red" style="width:58px">BOOK</a>
</article>
<article class="abs service" style="left:311px">
  <div class="service-head"><div class="service-icon" role="img" aria-label="Line icon of two people consulting at a desk"></div></div>
  <h3>CONTRACT CONSULTING</h3>
  <p>Lorem Ipsum is simply dummy text of the printing and typesetting industry. Lorem Ipsum has been the industry's standard dummy text ever since the 1500s, when an unknown printer took a galley of type and scrambled it to make a type specimen book.</p>
  <a class="btn-red" style="width:58px">APPOINTMENT</a>
</article>
<article class="abs service" style="left:464px">
  <div class="service-head"><div class="service-icon" role="img" aria-label="Line icon of a monitor with a reviewer and three stars"></div></div>
  <h3>CONTRACT REVIEW</h3>
  <p>Lorem Ipsum is simply dummy text of the printing and typesetting industry. Lorem Ipsum has been the industry's standard dummy text ever since the 1500s, when an unknown printer took a galley of type and scrambled it to make a type specimen book.</p>
  <a class="btn-red" style="width:58px">REQUEST</a>
</article>

<section class="abs video" role="img" aria-label="Video still of hands typing on a laptop beside printed charts">
  <svg class="abs" style="left:213px;top:80px" width="20" height="24" viewBox="0 0 20 24"><path d="M0 0L20 12L0 24Z" fill="#ffffff"/></svg>
  <div class="abs video-bar"><span></span></div>
  <svg class="abs" style="left:10px;bottom:3px" width="40" height="8" viewBox="0 0 40 8" fill="#ffffff">
    <rect x="1" y="1" width="1.6" height="6"/><rect x="4" y="1" width="1.6" height="6"/>
    <path d="M13 1l3.5 3-3.5 3zM16.5 1l3.5 3-3.5 3z"/><rect x="20" y="1" width="1" height="6"/>
    <path d="M27 3h2l2.5-2v6L29 5h-2z"/>
  </svg>
  <div class="abs video-time">0:35 / 2:25</div>
  <svg class="abs" style="right:8px;bottom:3px" width="56" height="8" viewBox="0 0 56 8" fill="none" stroke="#ffffff" stroke-width="1">
    <rect x="1" y="2" width="7" height="5"/><circle cx="19" cy="4.5" r="2.3"/><rect x="30" y="2" width="8" height="5"/>
    <path d="M46 2h2M46 2v2M53 2h-2M53 2v2M46 7h2M46 7v-2M53 7h-2M53 7v-2"/>
  </svg>
</section>

<section class="abs contact">
  <svg class="abs" style="left:22px;top:12px" width="26" height="18" viewBox="0 0 26 18" fill="none" stroke="#ffffff" stroke-width="1.2"><rect x="1" y="1" width="24" height="16"/><path d="M1 1l12 9 12-9M1 17l9-8M25 17l-9-8"/></svg>
  <div class="abs contact-text contact-email">EMAIL: INFO@CLAUSEWISE.EXAMPLE</div>
  <svg class="abs" style="left:238px;top:10px" width="24" height="24" viewBox="0 0 24 24" fill="none" stroke="#ffffff" stroke-width="1.2"><path d="M5 2l4 5-2 3c1.5 3 4 5.5 7 7l3-2 5 4-3 3C11 21 3 13 2 5z"/></svg>
  <div class="abs contact-text contact-phone">PHONE NUMBER: (123) 555 0147</div>
</section>

<h2 class="abs section-title" style="top:876px">TESTIMONIAL</h2>

<article class="abs quote" style="left:159px">
  <p>"Lorem Ipsum is simply dummy text of the printing and typesetting industry. Lorem Ipsum has been the industry's"</p>
  <div class="stars">★★★★★</div><h4>MARTEN HALE</h4>
</article>
<article class="abs quote" style="left:312px">
  <p>"Lorem Ipsum is simply dummy text of the printing and typesetting industry. Lorem Ipsum has been the industry's"</p>
  <div class="stars">★★★★★</div><h4>RINA SOTO</h4>
</article>
<article class="abs quote" style="left:464px">
  <p>"Lorem Ipsum is simply dummy text of the printing and typesetting industry. Lorem Ipsum has been the industry's"</p>
  <div class="stars">★★★★★</div><h4>IVY LAREN</h4>
</article>
<div class="abs avatar" style="left:206px;background:radial-gradient(circle at 50% 40%,#c9a27c,#6b4a34)" role="img" aria-label="Portrait photo of a bearded client"></div>
<div class="abs avatar" style="left:359px;background:radial-gradient(circle at 50% 40%,#e6c0a4,#7a3d2a)" role="img" aria-label="Portrait photo of a smiling client"></div>
<div class="abs avatar" style="left:511px;background:radial-gradient(circle at 50% 40%,#e8cfa0,#9a7448)" role="img" aria-label="Portrait photo of a client reading"></div>

<footer class="abs footer">
  <a href="#" style="left:159px;top:27px">Evaluation</a>
  <a href="#" style="left:159px;top:48px">Market Feedback</a>
  <a href="#" style="left:270px;top:27px">Students</a>
  <a href="#" style="left:270px;top:48px">Templates</a>
  <a href="#" style="left:381px;top:27px">Policies</a>
  <a href="#" style="left:381px;top:48px">Tools</a>
  <a href="#" style="left:493px;top:27px">Team</a>
  <a href="#" style="left:493px;top:48px">Contact</a>
</footer>
<div class="abs base">
  <div class="abs brand" style="left:160px;top:8px">Clausewise</div>
  <div class="abs legal">©2018 Clausewise.com</div>
</div>

</body>
</html>
```